Business cards design for T38 (Разработка визитных карточек)

We would like to get design of our business cards loosely based on our website design [url removed, login to view]

logo in vector is atteched

There should be following info to be present on business card:
Martin Colvey
CEO
T38
+7 (222) 222-22-22
+7 (222) 222-22-22
colvey@tessarine-mail.ru
222222, Moscow, Ulitsa Tikhvoronskaya, 7B

```html
<!DOCTYPE html>
<html lang="en">
<head>
<meta charset="utf-8">
<title>T38 — Business Cards</title>
<link rel="stylesheet" href="https://fonts.googleapis.com/css2?family=Oswald:wght@400;600&display=swap">
<style>
  :root {
    --bg: #2e2f31;
    --slate: #3f4650;
    --slate-deep: #353b44;
    --cream: #d8d3b1;
    --orange: #cf4a2c;
    --orange-deep: #a9341d;
    --orange-light: #e0633f;
    --font: "Oswald", sans-serif;
  }
  * { margin: 0; padding: 0; box-sizing: border-box; }
  html, body { width: 1200px; height: 749px; overflow: hidden; background: var(--bg); font-family: var(--font); }
  .stage { position: relative; width: 1200px; height: 749px; }
  .card {
    position: absolute; top: 214px; width: 540px; height: 320px;
    background: var(--slate); overflow: hidden;
    box-shadow: 0 14px 30px rgba(0,0,0,.45);
  }
  .card--front { left: 40px; }
  .card--back { left: 620px; }
  .card__shape { position: absolute; inset: 0; }

  .front__logo {
    position: absolute; left: 330px; top: 70px;
    font-size: 96px; font-weight: 600; line-height: 1; color: var(--orange);
    letter-spacing: 2px;
  }
  .front__identity { position: absolute; left: 34px; top: 62px; width: 200px; }
  .front__rule { height: 3px; background: var(--cream); margin-left: 86px; margin-bottom: 6px; }
  .front__name {
    font-size: 22px; font-weight: 600; color: var(--orange-deep);
    text-transform: uppercase; letter-spacing: .5px; line-height: 1;
    border-top: 3px solid var(--orange); padding-top: 3px; display: inline-block;
  }
  .front__role { font-size: 12px; color: var(--orange-deep); letter-spacing: 1px; margin-top: 2px; }

  .contacts { position: absolute; left: 34px; top: 192px; display: flex; gap: 12px; }
  .contacts__icons {
    width: 18px; background: var(--orange-deep);
    display: flex; flex-direction: column; justify-content: space-around; align-items: center;
    padding: 4px 0;
  }
  .contacts__icons svg { width: 11px; height: 11px; fill: var(--slate-deep); }
  .contacts__list { list-style: none; font-size: 11px; color: var(--orange-deep); text-transform: uppercase; line-height: 1.55; letter-spacing: .3px; }

  .back__window { position: absolute; left: 90px; top: 100px; width: 370px; height: 130px; }
  .back__logo {
    position: absolute; left: 90px; top: 100px; width: 370px; height: 130px;
    display: flex; align-items: center; justify-content: center;
    font-size: 100px; font-weight: 600; color: var(--slate); letter-spacing: 4px; line-height: 1;
  }
</style>
</head>
<body>
<main class="stage">

  <section class="card card--front" aria-label="Business card front">
    <svg class="card__shape" viewBox="0 0 540 320" aria-hidden="true">
      <path d="M236 0 C204 62 222 124 300 172 C390 226 470 246 540 256 L540 0 Z" fill="var(--orange)" transform="translate(-6 4)"/>
      <path d="M236 0 C204 62 222 124 300 172 C390 226 470 246 540 256 L540 0 Z" fill="var(--cream)"/>
    </svg>
    <div class="front__logo">T38</div>
    <div class="front__identity">
      <div class="front__rule"></div>
      <div class="front__name">Martin Colvey</div>
      <div class="front__role">CEO</div>
    </div>
    <div class="contacts">
      <div class="contacts__icons">
        <svg viewBox="0 0 12 12"><path d="M2 1h3l1 3-2 1a7 7 0 0 0 3 3l1-2 3 1v3c-6 0-10-4-9-9z"/></svg>
        <svg viewBox="0 0 12 12"><path d="M1 3h10v7H1z M1 3l5 4 5-4" /></svg>
        <svg viewBox="0 0 12 12"><circle cx="6" cy="6" r="5"/></svg>
        <svg viewBox="0 0 12 12"><path d="M6 1a4 4 0 0 1 4 4c0 3-4 7-4 7S2 8 2 5a4 4 0 0 1 4-4z"/></svg>
      </div>
      <ul class="contacts__list">
        <li>+7 (222) 222-22-22</li>
        <li>+7 (222) 222-22-22</li>
        <li>colvey@tessarine-mail.ru</li>
        <li>www.t38-studio.ru</li>
        <li>222222, Moscow, Ulitsa Tikhvoronskaya,<br>7B</li>
      </ul>
    </div>
  </section>

  <section class="card card--back" aria-label="Business card back">
    <svg class="back__window" viewBox="0 0 370 130" preserveAspectRatio="none" aria-hidden="true">
      <defs>
        <linearGradient id="windowTone" x1="0" y1="0" x2="0" y2="1">
          <stop offset="0" stop-color="var(--orange-light)"/>
          <stop offset="1" stop-color="var(--orange-deep)"/>
        </linearGradient>
      </defs>
      <rect width="370" height="130" fill="url(#windowTone)"/>
      <g stroke="var(--orange-deep)" stroke-width="1.5" opacity=".7">
        <line x1="0" y1="16" x2="370" y2="16"/><line x1="0" y1="32" x2="370" y2="32"/>
        <line x1="0" y1="48" x2="370" y2="48"/><line x1="0" y1="64" x2="370" y2="64"/>
        <line x1="0" y1="80" x2="370" y2="80"/><line x1="0" y1="96" x2="370" y2="96"/>
        <line x1="0" y1="112" x2="370" y2="112"/>
      </g>
      <rect x="0" y="0" width="370" height="6" fill="rgba(0,0,0,.25)"/>
    </svg>
    <div class="back__logo">T38</div>
  </section>

</main>
</body>
</html>
```